professional coaching and counselling service elegant brochure

Harbourlight Steps is a professional coaching and counseling business that works with organizations to provide psychological support to working mums, dads and managers before and after the birth of a child.

We need an elegant and professional brochure that we can provide to clients as a ‘pitch’ document that provides an overview of our services. The document will be used in emails and and to hand out at networking events to introduce Harbourlight Steps to potential clients. The aim is that a client will get a feeling for Harbourlight Steps and be able to read about the services offered.

The colors need to be in line with the greens and blues of our attached logos to provide a warm feel. I have attached a number of images that represent the offer and target market as a guide.

We have provided the text it will probably be a two page brochure but will by guided by your creativity as to how it is best laid out. See attached word document.

Font and layout are open to creativity. Looking for A4 size

Target Market(s)

professionals and executives working in large organisations

Industry/Entity Type

Psychology

Requirements
Must have
• warmth, engaging, elegant and professional feel
Should not have
• anything offensive, harsh colors

```html
<!DOCTYPE html>
<html lang="en">
<head>
<meta charset="utf-8">
<title>Harbourlight Steps – Brochure</title>
<link rel="stylesheet" href="https://fonts.googleapis.com/css2?family=Oswald:wght@400;500&family=Open+Sans:ital,wght@0,400;0,700;1,400&display=swap">
<style>
  :root {
    --green: #8cc63f;
    --green-deep: #6fb52c;
    --green-text: #7cbf3a;
    --blue: #1c8fc9;
    --blue-deep: #1675a8;
    --blue-light: #4fb3e3;
    --grey-band: #c9cdd1;
    --ink: #5a5f63;
    --paper: #ffffff;
    --backdrop: #ebe8e3;
  }
  * { box-sizing: border-box; margin: 0; padding: 0; }
  html, body { width: 1200px; height: 729px; overflow: hidden; background: var(--backdrop); }
  .canvas { position: relative; width: 1200px; height: 729px; overflow: hidden; font-family: "Open Sans", Arial, sans-serif; color: var(--ink); }

  /* ---------- inside spread ---------- */
  .spread { position: absolute; left: 90px; top: 95px; width: 735px; height: 540px; background: var(--paper); box-shadow: 0 4px 14px rgba(0,0,0,.18); overflow: hidden; }
  .photo-strip { position: absolute; left: 0; top: 0; width: 735px; height: 125px; display: flex; }
  .photo-strip .block { height: 125px; }
  .block--blue { background: var(--blue); }
  .block--blue-light { background: var(--blue-light); }
  .photo { background: linear-gradient(135deg, #e9e2da 0%, #cfc4b8 55%, #9fb8c6 100%); }
  .photo--cool { background: linear-gradient(135deg, #dfe4e6 0%, #c3cdd2 50%, #8fa9b8 100%); }
  .photo--warm { background: linear-gradient(135deg, #efe6dc 0%, #d7c5b2 60%, #b7a490 100%); }

  .panel { position: absolute; top: 125px; width: 245px; height: 400px; }
  .panel--about { left: 0; background: var(--green); color: #fff; }
  .panel--program { left: 245px; background: var(--paper); }
  .panel--benefits { left: 490px; background: var(--paper); }

  .panel-title { font-family: "Oswald", "Arial Narrow", sans-serif; font-weight: 500; text-transform: uppercase; line-height: 1.02; }
  .panel--about .panel-title { position: absolute; left: 20px; top: 24px; font-size: 20px; color: #fff; }
  .panel--program .panel-title { position: absolute; left: 20px; top: 24px; font-size: 20px; color: var(--green-text); }
  .panel--benefits .panel-title { position: absolute; left: 18px; top: 24px; font-size: 20px; color: var(--blue); }

  .body-copy { font-size: 6.4px; line-height: 1.5; }
  .panel--about .body-copy { position: absolute; left: 20px; top: 78px; width: 212px; }
  .panel--program .body-copy { position: absolute; left: 20px; top: 100px; width: 212px; }
  .body-copy p + p { margin-top: 7px; }
  .body-copy .lead-out { font-style: italic; color: var(--green-text); }

  .about-photo { position: absolute; left: 0; bottom: 0; width: 245px; height: 215px; background: linear-gradient(180deg, var(--green) 0%, #a8d66a 40%, #b9df85 70%, var(--green) 100%); }

  .program-name { position: absolute; left: 78px; top: 320px; font-family: "Oswald", "Arial Narrow", sans-serif; font-weight: 500; font-size: 22px; letter-spacing: 1px; color: var(--green-deep); }

  .benefit-list { position: absolute; left: 18px; top: 62px; width: 214px; list-style: none; }
  .benefit { display: flex; align-items: flex-start; gap: 8px; height: 40px; }
  .benefit-icon { flex: 0 0 20px; width: 20px; height: 20px; background: var(--blue); display: flex; align-items: center; justify-content: center; }
  .benefit-icon svg { width: 13px; height: 13px; }
  .benefit-text { font-size: 6.2px; line-height: 1.4; }
  .benefit-title { display: block; font-weight: 700; color: var(--blue); font-size: 6.6px; }

  .foot-bands { position: absolute; left: 0; bottom: 0; width: 735px; height: 15px; display: flex; }
  .foot-bands span { height: 15px; }

  /* ---------- front cover ---------- */
  .cover { position: absolute; left: 865px; top: 95px; width: 245px; height: 540px; background: var(--paper); box-shadow: 0 4px 14px rgba(0,0,0,.18); overflow: hidden; }
  .cover-title { position: absolute; left: 14px; top: 30px; font-family: "Oswald", "Arial Narrow", sans-serif; font-weight: 500; text-transform: uppercase; font-size: 16px; line-height: 1.12; white-space: nowrap; }
  .cover-title .line-green { display: block; color: var(--green-text); }
  .cover-title .line-blue { display: block; color: var(--blue); }
  .cover-photo { position: absolute; left: 0; top: 82px; width: 245px; height: 458px; background: linear-gradient(170deg, #eef1f2 0%, #dde3e6 35%, #b3c6d3 65%, #7fa1bb 85%, #4f8fb8 100%); }
  .cover-brand { position: absolute; right: 14px; top: 205px; display: flex; align-items: center; gap: 5px; font-family: "Oswald", "Arial Narrow", sans-serif; font-weight: 500; font-size: 11px; color: var(--blue); text-transform: uppercase; }
  .cover-brand .dot { width: 8px; height: 8px; border-radius: 50%; background: var(--green); }
</style>
</head>
<body>
<div class="canvas">

  <section class="spread">
    <div class="photo-strip">
      <div class="block block--blue" style="width:30px"></div>
      <div class="photo photo--warm block" style="width:130px" role="img" aria-label="Photo of a smiling mother holding her baby"></div>
      <div class="block block--blue-light" style="width:55px"></div>
      <div class="photo block" style="width:120px" role="img" aria-label="Photo of a pregnant woman working on a laptop at home"></div>
      <div class="block block--blue" style="width:40px"></div>
      <div class="photo photo--cool block" style="width:150px" role="img" aria-label="Photo of a father and mother with their baby in a kitchen"></div>
      <div class="block block--blue-light" style="width:35px"></div>
      <div class="photo photo--warm block" style="width:135px" role="img" aria-label="Photo of a businessman at his desk with a toddler"></div>
      <div class="block block--blue" style="width:40px"></div>
    </div>

    <div class="panel panel--about">
      <h2 class="panel-title">About<br>Harbourlight Steps</h2>
      <div class="body-copy">
        <p>At Harbourlight Steps we specialise in supporting management and parents in navigating this significant transition. Not only are we about assisting you to meet best legal and diversity requirements, our unique KEYSTONE™ Parental Leave Transition Program supports you and your staff to exceed these expectations, and develop relationships that work for both parties. All Harbourlight Steps consultants are registered psychologists and accredited to run the KEYSTONE™ program nationally.</p>
      </div>
      <div class="about-photo" role="img" aria-label="Green-tinted photo of a pregnant woman sitting cross-legged"></div>
    </div>

    <div class="panel panel--program">
      <h2 class="panel-title">About the<br>Keystone Parental Leave<br>Transition Program</h2>
      <div class="body-copy">
        <p>Specific to the Parental Leave Transition, and in association with the Institute for Family Leave Studies (USA), we have developed a researched and practice-based coaching program to maximise transition success into, through and returning from Parental Leave.</p>
        <p>While traditionally a form of leadership coaching, we have developed a digital solution to enable an enriched experience that is cost effective and scalable across all levels of an organisation – from a fully digital offering right through to a highly individualised and personal experience. With this increased capability, we are able to deliver ‘just in time’ education and resources to both managers and employees (maternity and paternity).</p>
        <p class="lead-out">The KEYSTONE™ Parental Leave Transition Program offers an innovative solution to cost and accessibility issues in supporting your people through the Parental Leave Transition.</p>
      </div>
      <div class="program-name">KEYSTONE</div>
    </div>

    <div class="panel panel--benefits">
      <h2 class="panel-title">Benefits to Business</h2>
      <ul class="benefit-list">
        <li class="benefit">
          <span class="benefit-icon"><svg viewBox="0 0 13 13"><rect x="2" y="1" width="2" height="11" fill="#fff"/><rect x="9" y="1" width="2" height="11" fill="#fff"/><rect x="2" y="5.5" width="9" height="2" fill="#fff"/></svg></span>
          <span class="benefit-text"><span class="benefit-title">Employee Retention:</span>Retain employees and avoid disruptive and expensive replacement costs.</span>
        </li>
        <li class="benefit">
          <span class="benefit-icon"><svg viewBox="0 0 13 13"><rect x="1" y="8" width="2.5" height="4" fill="#fff"/><rect x="5" y="5" width="2.5" height="7" fill="#fff"/><rect x="9" y="2" width="2.5" height="10" fill="#fff"/></svg></span>
          <span class="benefit-text"><span class="benefit-title">Business Continuity:</span>Reduce the negative impacts of leave upon client relationships and work teams.</span>
        </li>
        <li class="benefit">
          <span class="benefit-icon"><svg viewBox="0 0 13 13"><circle cx="6.5" cy="6.5" r="5" fill="none" stroke="#fff" stroke-width="1.5"/><circle cx="6.5" cy="6.5" r="1.8" fill="#fff"/></svg></span>
          <span class="benefit-text"><span class="benefit-title">Employer of Choice Branding:</span>Enhance reputation as a socially aware and “Family Friendly” employer.</span>
        </li>
        <li class="benefit">
          <span class="benefit-icon"><svg viewBox="0 0 13 13"><rect x="2" y="2" width="6" height="3" fill="#fff" transform="rotate(-30 5 3.5)"/><rect x="5.5" y="5" width="1.6" height="7" fill="#fff" transform="rotate(-30 6.3 8.5)"/><rect x="1" y="11" width="7" height="1.5" fill="#fff"/></svg></span>
          <span class="benefit-text"><span class="benefit-title">Mitigate Risk and Promote WHS:</span>Manage legal risk and create a safe workplace around transition.</span>
        </li>
        <li class="benefit">
          <span class="benefit-icon"><svg viewBox="0 0 13 13"><rect x="5" y="1" width="3" height="11" fill="#fff"/><rect x="1" y="5" width="11" height="3" fill="#fff"/></svg></span>
          <span class="benefit-text"><span class="benefit-title">Improve Health and Well-being:</span>Proactively address transition to promote sound employee health and well-being.</span>
        </li>
        <li class="benefit">
          <span class="benefit-icon"><svg viewBox="0 0 13 13"><circle cx="4" cy="4" r="2" fill="#fff"/><rect x="1.5" y="7" width="5" height="5" rx="1" fill="#fff"/><circle cx="9.5" cy="5" r="1.6" fill="#fff"/><rect x="7.5" y="7.5" width="4" height="4.5" rx="1" fill="#fff"/></svg></span>
          <span class="benefit-text"><span class="benefit-title">Normalise Support:</span>Reduce stigma and address identified barriers to help seeking.</span>
        </li>
        <li class="benefit">
          <span class="benefit-icon"><svg viewBox="0 0 13 13"><circle cx="5" cy="7.5" r="3" fill="none" stroke="#fff" stroke-width="1.4"/><circle cx="8" cy="5" r="3" fill="none" stroke="#fff" stroke-width="1.4"/></svg></span>
          <span class="benefit-text"><span class="benefit-title">Gender Diversity:</span>Help achieve gender diversity and reporting requirements.</span>
        </li>
        <li class="benefit">
          <span class="benefit-icon"><svg viewBox="0 0 13 13"><circle cx="6.5" cy="3.5" r="2.2" fill="#fff"/><path d="M2 12 Q6.5 5 11 12 Z" fill="#fff"/></svg></span>
          <span class="benefit-text"><span class="benefit-title">Career Re-Engagement:</span>Equip employees to successfully and sustainably re-enter the workforce.</span>
        </li>
      </ul>
    </div>

    <div class="foot-bands">
      <span style="width:245px;background:var(--green)"></span>
      <span style="width:125px;background:var(--blue)"></span>
      <span style="width:235px;background:var(--grey-band)"></span>
      <span style="width:130px;background:var(--green)"></span>
    </div>
  </section>

  <section class="cover">
    <h1 class="cover-title">
      <span class="line-green">Harbourlight Steps:</span>
      <span class="line-blue">Navigating Work-Life Change</span>
    </h1>
    <div class="cover-photo" role="img" aria-label="Photo of a smiling pregnant woman on the phone at a home office desk"></div>
    <div class="cover-brand"><span class="dot"></span>Harbourlight Steps</div>
  </section>

</div>
</body>
</html>
```